Recycling Exhibition Web Design Project

We are developing a new website for a exhibition we have just taken over. The previous site is very basic and we require a complete redesign. The site should be designed to engage with and attract those who work in or provide services to the multibillion dollar wastes and recycling industry in the Asia pacific region. These will include Federal & State Governments, City councils, private sector, industry associations and other key bodies, education facilities.

KTLO is the premier waste and recycling event in the Asia Pacific region and known as place where the industry meets to share innovations, gain knowledge, to network and do business.
• Innovation
• Knowledge transfer
• Industry Networking
• Trade
Key point: need to reflect that 2012 show will attract large numbers of quality visitors from across wide range of the industry – city councils, facilities managers, etc

Site should deliver 3 key objectives.
1. Stimulate interest those who work in or provide services to the wastes and recycling industry by providing simple to access, relevant and topical information about the Expo, the Seminars, the Key Features, the sub activities and the key benefits to them.
2. Provide a platform that supports / improves EP by providing a range of interactive components – ie floor plan / video. In addition options for sales enquiries, registration, general feedback
3. Provide a way to highlight / showcase sponsors, show features and other key assets. (possibly a carousel above the fold)

We really like the dunmar website so a take on this could be good (http://www.dunmar-example.com.au/). Also we want to try to reinforce the brand so we should use the event as the hero image/banner.

Previous website - http://www.ktlo-example.com.au/

Target Market(s)

The site should be designed to engage with and attract those who work in or provide services to the multibillion dollar wastes and recycling industry

Industry/Entity Type

Recycling

Requirements
Must have
• The icons on the current site work quite well so inclusion as CTAs would be preferable.

Other key areas are

• Seminar Delegate & Visitor Registration
• Exhibitor Prospectus
• Floorplan
• Conference / Seminar content
• Social media + blog

Site visitors will need to feel like they are part of a community.
Site should reflect/display key industry stats & stats from 2011 expo

Please see the attached brief for more details and site map for menu items.

```html
<!DOCTYPE html>
<html lang="en">
<head>
<meta charset="utf-8">
<title>KTLO Waste &amp; Recycling Expo 2012</title>
<link href="https://fonts.googleapis.com/css2?family=Archivo:wght@700;800;900&family=Arimo:wght@400;700&family=Open+Sans:wght@400;600&display=swap" rel="stylesheet">
<style>
:root{
  --ink:#1b1b1b;
  --lime:#bdd73f;
  --orange:#f47b20;
  --red:#c0392b;
  --green:#5e7a3a;
  --paper:#ebe7de;
  --grey-band:#dcdcdc;
  --heading-grey:#8a8a8a;
  --white:#fff;
  --text:#111;
  --muted:#9a9a9a;
}
*{box-sizing:border-box;margin:0;padding:0}
html,body{width:908px;height:1200px;overflow:hidden}
body{position:relative;background:var(--paper);font-family:"Arimo",Arial,sans-serif;color:var(--text)}
.site-header{position:absolute;top:0;left:0;width:908px;height:72px;background:var(--ink)}
.brand{position:absolute;left:108px;top:14px;display:flex;align-items:center;gap:8px;color:var(--white);font-family:"Archivo",sans-serif;font-weight:800;font-size:22px;letter-spacing:.5px}
.brand-dot{width:26px;height:26px;border-radius:50%;background:var(--orange)}
.event-info{position:absolute;right:108px;top:16px;text-align:right;font-family:"Open Sans",sans-serif}
.event-date{color:#d9372a;font-size:21px;line-height:24px}
.event-venue{color:var(--white);font-size:16px;line-height:22px}
.main-nav{position:absolute;top:72px;left:0;width:908px;height:28px;background:var(--lime)}
.main-nav ul{list-style:none;position:absolute;left:108px;top:0;height:28px;display:flex}
.main-nav li{height:28px;line-height:30px;font-size:11px;letter-spacing:.6px;color:#222;text-transform:uppercase;padding:0 0 0 21px;width:auto}
.main-nav li.home{background:var(--orange);width:80px;padding:0;text-align:center;border-top:3px solid #f6a04c;line-height:25px}
.main-nav li.show{width:104px}.main-nav li.whats{width:106px}.main-nav li.reg{width:98px}
.main-nav li.exhibit{width:136px}.main-nav li.blog{width:74px}
.side-tab{position:absolute;top:156px;width:30px;height:112px;display:flex;align-items:center;justify-content:center;border:2px solid var(--white);outline:1px solid #999}
.side-tab span{writing-mode:vertical-rl;color:var(--white);font-family:"Archivo",sans-serif;font-weight:800;font-size:12px;letter-spacing:.5px}
.tab-register{left:0;background:var(--red)}
.tab-follow{right:0;background:var(--ink)}
.tab-follow span{transform:rotate(180deg)}
.hero-title{position:absolute;top:138px;left:0;width:908px;text-align:center;font-family:"Archivo",sans-serif;font-weight:800;font-size:23px;color:var(--heading-grey)}
.hero-art{position:absolute;left:166px;top:194px;width:578px;height:286px;border-radius:140px;background:linear-gradient(90deg,#ec6a2c 0%,#ec6a2c 38%,#5f7c3c 50%,#5f7c3c 100%);opacity:.9}
.sponsors{position:absolute;top:517px;left:0;width:908px;height:73px;background:var(--white)}
.sponsors h2{position:absolute;left:108px;top:19px;font-family:"Archivo",sans-serif;font-weight:800;font-size:16px;line-height:18px;color:var(--ink)}
.sponsors svg.brace{position:absolute;left:203px;top:8px}
.badge{position:absolute;top:18px}
.about{position:absolute;top:590px;left:0;width:908px;height:138px;background:var(--grey-band);border-bottom:2px solid var(--white)}
.about h1{position:absolute;left:108px;top:29px;font-family:"Archivo",sans-serif;font-weight:700;font-size:18px;color:var(--red)}
.about p{position:absolute;left:108px;top:57px;width:694px;font-size:11px;line-height:14px;font-weight:700}
.feature{position:absolute;top:762px;width:224px;height:140px;background:var(--ink)}
.feature .media{height:107px}
.feature h3{color:var(--white);font-family:"Archivo",sans-serif;font-weight:700;font-size:15px;padding:8px 6px}
.feature-seminars{left:108px}.feature-seminars .media{background:linear-gradient(135deg,#2c2420,#6b4a3a 60%,#3b2e28)}
.feature-prospectus{left:343px}.feature-prospectus .media{background:linear-gradient(180deg,#9fd1ec 0%,#b7dcec 40%,#8a9a80 70%,#c9a040 100%)}
.feature-floorplan{left:577px}.feature-floorplan .media{background:var(--white)}
.news-label{position:absolute;left:108px;top:962px;font-family:"Archivo",sans-serif;font-weight:800;font-size:24px;line-height:28px;color:var(--heading-grey)}
.news-brace{position:absolute;left:300px;top:932px}
.news-item{position:absolute;left:342px;top:944px;width:460px}
.news-item h2{font-family:"Archivo",sans-serif;font-weight:700;font-size:16px;color:var(--orange);margin-bottom:6px}
.news-item p{font-size:10px;line-height:13px}
.read-more{color:var(--red);font-size:8px;font-weight:700;text-transform:uppercase;margin-left:4px}
.site-footer{position:absolute;top:1082px;left:0;width:908px;height:118px;background:var(--ink)}
.footer-nav{position:absolute;left:108px;top:26px;display:flex;list-style:none;color:var(--white);font-size:10px}
.footer-nav li{padding-right:7px;margin-right:7px;border-right:3px solid var(--white);line-height:10px}
.footer-nav li:last-child{border:0}
.newsletter{position:absolute;left:108px;top:46px;display:flex;gap:4px}
.newsletter .field{width:180px;height:17px;background:var(--white);font-size:8px;color:#777;line-height:17px;padding-left:6px}
.newsletter .submit{width:62px;height:17px;background:var(--red);border:1px solid var(--white);color:var(--white);font-size:9px;font-weight:700;text-align:center;line-height:15px}
.social{position:absolute;left:108px;top:72px;display:flex;gap:4px}
.social span{width:17px;height:17px}
.publisher{position:absolute;right:108px;top:28px;text-align:right;color:var(--muted);font-size:8px;line-height:10px}
.publisher strong{display:block;font-family:"Archivo",sans-serif;font-size:15px;line-height:18px;color:#bbb;margin-bottom:3px}
</style>
</head>
<body>
<header class="site-header">
  <div class="brand"><span class="brand-dot"></span>KTLO Expo</div>
  <div class="event-info">
    <div class="event-date">21 &amp; 22 November 2012</div>
    <div class="event-venue">Harbourside Convention Centre</div>
  </div>
</header>
<nav class="main-nav">
  <ul>
    <li class="home">Home</li><li class="show">The Show</li><li class="whats">What's On</li><li class="reg">Register</li><li class="exhibit">How to Exhibit</li><li class="blog">Blog</li><li>Contact</li>
  </ul>
</nav>
<a class="side-tab tab-register"><span>Register FREE</span></a>
<a class="side-tab tab-follow"><span>Follow Us On</span></a>

<h2 class="hero-title">What is next in Waste, Recycling &amp; Sustainability?</h2>
<div class="hero-art" role="img" aria-label="Two speech bubbles filled with recycling, bin, truck and light bulb icons in orange and green"></div>

<section class="sponsors">
  <h2>Sponsors &amp;<br>Partners</h2>
  <svg class="brace" width="16" height="58" viewBox="0 0 16 58"><path d="M2 2 Q10 2 10 10 V22 Q10 29 15 29 Q10 29 10 36 V48 Q10 56 2 56" fill="none" stroke="#1b1b1b" stroke-width="2"/></svg>
  <svg class="badge" style="left:240px" width="40" height="40"><circle cx="20" cy="20" r="18" fill="#0f3b5f"/></svg>
  <svg class="badge" style="left:390px" width="30" height="40"><rect x="2" y="2" width="26" height="34" rx="6" fill="#e85a8a"/></svg>
  <svg class="badge" style="left:462px" width="120" height="40"><rect x="0" y="14" width="120" height="12" rx="6" fill="#3da44a"/></svg>
  <svg class="badge" style="left:590px" width="46" height="46"><circle cx="23" cy="20" r="20" fill="#2d8a2d"/></svg>
  <svg class="badge" style="left:676px" width="44" height="40"><rect x="4" y="4" width="36" height="26" rx="13" fill="#c0392b"/></svg>
  <svg class="badge" style="left:758px" width="44" height="40"><rect x="0" y="0" width="44" height="40" fill="#1b2a4a"/></svg>
</section>

<section class="about">
  <h1>KTLO Waste &amp; Recycling Expo 2012</h1>
  <p>KTLO Waste &amp; Recycling Expo (KTLO) is the biggest trade show for the waste and recycling industry in Australasia. A full program of presentations will be coordinated. Presentations given by experts from around the world will attract industry professionals to the Expo. Trade Delegates attending the Trade Expo only will be free. Networking functions will be organised to ensure you have the opportunity to discuss business with clients and/or colleagues.</p>
</section>

<article class="feature feature-seminars"><div class="media" role="img" aria-label="Speaker presenting at a seminar"></div><h3>Seminars }</h3></article>
<article class="feature feature-prospectus"><div class="media" role="img" aria-label="Seedling growing from a pile of recycled cans"></div><h3>Exhibitor Prospectus }</h3></article>
<article class="feature feature-floorplan"><div class="media" role="img" aria-label="Exhibition floorplan with green stand blocks" style="background:repeating-linear-gradient(90deg,#fff 0 4px,#0b7a0b 4px 40px,#fff 40px 44px),#fff;background-size:44px 100%"></div><h3>Floorplan }</h3></article>

<h2 class="news-label">Latest News &amp;<br>Updates</h2>
<svg class="news-brace" width="26" height="118" viewBox="0 0 26 118"><path d="M4 3 Q16 3 16 16 V46 Q16 58 24 59 Q16 60 16 72 V102 Q16 115 4 115" fill="none" stroke="#8a8a8a" stroke-width="4"/></svg>
<article class="news-item">
  <h2>Lorem Ipsum Dolor Sit Amet</h2>
  <p>Lorem ipsum dolor sit amet, consectetur adipiscing elit. Aliquam mollis nibh sed diam condimentum placerat sed a nisi. In hac habitasse platea dictumst. Nunc dui neque, accumsan quis interdum vel, molestie ac mauris. Nam sollicitudin, lectus sed vulputate porta, orci odio dignissim risus, dictum consectetur dui nisl eget purus. Sed vel dui id dui sodales faucibus. Pellentesque suscipit odio sit amet sem viverra id tincidunt leo mattis. Curabitur posuere fringilla erat, sit amet sollicitudin mi dapibus vel. <span class="read-more">Read more</span></p>
</article>

<footer class="site-footer">
  <ul class="footer-nav"><li>HOME</li><li>THE SHOW</li><li>WHAT'S ON</li><li>REGISTER</li><li>HOW TO EXHIBIT</li><li>BLOG</li><li>CONTACT</li></ul>
  <div class="newsletter"><div class="field">Sign up for our Newsletter</div><div class="submit">Submit</div></div>
  <div class="social"><span style="background:#2f64c4"></span><span style="background:#2aa3e0"></span><span style="background:#1a6fb0"></span><span style="background:#f07a20"></span></div>
  <div class="publisher">
    <strong>Meridian</strong>
    ©2012 Meridian Exhibitions.<br>
    Level 2, 118 Quay Street, NSW 2000<br>
    info@ktlo-example.com.au &nbsp;|&nbsp; +61 2 5550 1234
  </div>
</footer>
</body>
</html>
```